St Patrick’s Day home page website design

(UPDATED completion time and $ amount)

This is for a St Patrick’s Day Parade group. We need a new home page website redesign that has a very clean, professional but fun look and feel. <details below and attached>

This is for a St Patrick’s Day Parade group. We need a new home page website redesign that has a very clean, professional but fun look and feel. <See details below>

Photoshop size 1920 px wide. JPGs can be used as a preview, but final file needs to be a layered, live Photoshop file with “labeled layers” and any fonts used.

Examples are needed for 4pm EST (GMT -6) Saturday, September 18th.
Sites client likes:
https://www.tallmeadowmarch-example.org/
https://harborsidefestival-example.org/
<<<<<<<<<<<<<<<<<<<<<<<<<<<<<
-Current site: https://lanternsonthehill-example.com
-Green is the main color, white and orange are the accent colors

Main Logo:
-(see attached) St. Patrick’s Day - Parade Lanterns on the Hill
-Place in header
Event logo:
-(See Attached) The 35th Annual Lanterns on the Hill Parade
-Possibly in the header?
-Possibly just use “35th Annual” text and not the logo
Icons sitewide:
-Facebook
-Twitter
-Instagram
-My Cart icon

Navigation:
-Info
-About
-Gallery
-Links
-Parade Sponsors
-Store
-Blog
-Contact Us

Slide Show:
-Large image to fill right to left (with some type of slide indicator)
-Use attached image as a place holder

Home Page Module blocks: (just under slide show)
-Store (User shopping cart)
-Sign up for Run (Use Meadowlark Dash logo)
-Parade Magazine (Use Magazine image)
-Participant Portal (can use current people icon or something new)

Highlight section 1: (somewhere under home page blocks)
-History
-Route
-Countdown (like the Boston site https://harborsidefestival-example.org/)
-Registration
-Tomfoolery Bulletin Signup
Footer section:
Small Parade logo

Footer Navigation:
-Info
-About
-Gallery
-Links
-Parade Sponsors
-Store
-Blog
-Contact Us

Footer Icons:
-Facebook
-Twitter
-Instagram

© Copyright 2021 The Hollowbrook Group LLC - All right reserved.

```html
<!DOCTYPE html>
<html lang="en">
<head>
<meta charset="utf-8">
<title>Lanterns on the Hill Parade</title>
<link rel="stylesheet" href="https://fonts.googleapis.com/css2?family=Inter:wght@400;500;600;700&family=Outfit:wght@500;600;700&display=swap">
<style>
:root{
  --green:#3bae49;
  --green-dark:#2f9a3c;
  --yellow:#f2c500;
  --white:#ffffff;
  --page:#f4f4f4;
  --ink:#1d1d1d;
  --muted:#9a9a9a;
  --field:#f5f5f5;
  --field-ok:#eef8ee;
}
*{margin:0;padding:0;box-sizing:border-box}
html,body{width:1200px;height:3541px;overflow:hidden}
body{position:relative;background:var(--page);font-family:"Inter",sans-serif;color:var(--ink)}
.abs{position:absolute}
.heading{font-family:"Outfit",sans-serif;font-weight:600}

/* header & footer */
.site-header{top:0;left:0;width:1200px;height:107px;background:var(--green)}
.nav{top:0;height:107px;display:flex;align-items:center;gap:40px;font-size:14px;color:var(--white)}
.nav-left{left:206px}
.nav-right{left:708px}
.brand{left:543px;top:23px;width:113px;height:61px;background:var(--white);border-radius:2px;display:flex;align-items:center;justify-content:center;gap:6px;padding:0 6px;font-family:"Outfit",sans-serif;font-weight:600;font-size:12px;line-height:1.15;color:var(--green);text-align:center}
.brand i{flex:none;width:10px;height:10px;background:var(--green)}
.cart-btn{left:1075px;top:34px;width:42px;height:42px;background:var(--white);display:flex;align-items:center;justify-content:center}

/* hero */
.hero{top:107px;left:0;width:1200px;height:560px;background:linear-gradient(100deg,#3d5f8a 0%,#6b4a3a 25%,#4e5a45 50%,#3c4a3d 75%,#6a6560 100%)}
.hero-shade{inset:0;background:rgba(0,0,0,.28)}
.hero-title{top:126px;left:0;width:1200px;text-align:center;color:var(--white);font-size:46px;line-height:55px;font-weight:600}
.hero-text{top:270px;left:0;width:1200px;text-align:center;color:var(--white);font-size:13px;line-height:22px}
.btn{display:flex;align-items:center;justify-content:center;background:var(--green);color:var(--white);font-size:12px;font-weight:600;border-radius:3px}
.hero-btn{top:371px;left:529px;width:142px;height:50px;text-transform:uppercase;font-size:11px}
.dots{top:511px;left:541px;display:flex;gap:14px}
.dots span{width:12px;height:12px;border-radius:50%;background:var(--white)}
.dots span.on{background:var(--green)}

/* modules */
.module{top:770px;width:220px;margin-left:-110px;text-align:center}
.module-icon{height:96px;display:flex;align-items:center;justify-content:center}
.module-label{margin-top:36px;font-family:"Outfit",sans-serif;font-weight:600;font-size:19px}
.module .btn{margin:30px auto 0;width:142px;height:48px}
.ph{display:block}

/* countdown */
.countdown{top:1063px;left:0;width:1200px;height:250px;background:var(--green)}
.band-title{left:85px;color:var(--white);font-size:48px;line-height:55px}
.band-title em{font-style:normal;color:var(--yellow)}
.count{top:79px;width:125px;text-align:center}
.count-box{height:64px;background:var(--white);border-radius:3px;display:flex;align-items:center;justify-content:center;font-family:"Outfit",sans-serif;font-weight:600;font-size:40px;color:var(--green)}
.count-label{margin-top:16px;color:var(--white);font-family:"Outfit",sans-serif;font-weight:500;font-size:19px}

/* story blocks */
.eyebrow{font-size:10px;font-weight:600;color:var(--muted);text-transform:uppercase;letter-spacing:.3px}
.story-title{font-size:35px;line-height:45px;color:var(--green)}
.story-text{font-size:13.5px;line-height:25px;color:var(--ink);width:450px}
.photo{width:449px;height:289px}

/* registration */
.registration{top:2275px;left:0;width:1200px;height:250px;background:var(--green)}
.reg-text{left:443px;top:97px;width:470px;color:var(--white);font-size:13.5px;line-height:25px}
.reg-btn{left:959px;top:102px;width:156px;height:47px;background:var(--white);color:var(--green);font-size:12px;font-weight:700;border-radius:3px;display:flex;align-items:center;justify-content:center;letter-spacing:.3px}

/* subscribe */
.runners{top:2525px;left:0;width:1200px;height:476px;background:linear-gradient(90deg,#3f5a3a 0%,#5b4f4a 35%,#3d4a44 65%,#5a4a48 100%)}
.card{top:2683px;left:308px;width:584px;height:481px;background:var(--white);box-shadow:0 2px 8px rgba(0,0,0,.12)}
.card .eyebrow{position:absolute;left:87px;top:66px}
.card-title{left:87px;top:100px;font-size:35px;line-height:51px;color:var(--green)}
.card-title em{font-style:normal;color:var(--yellow)}
.field{left:87px;width:410px;height:49px;background:var(--field);border-radius:2px;font-size:11px;padding:0 20px}
.field.ok{top:230px;background:var(--field-ok)}
.field.ok small{display:block;padding-top:8px;font-size:7px;color:var(--muted)}
.field.ok b{display:block;font-weight:500;margin-top:4px}
.field.ok svg{position:absolute;right:20px;top:18px}
.field.email{top:296px;line-height:49px;color:var(--muted)}
.sub-btn{left:87px;top:377px;width:141px;height:41px}

.site-footer{top:3274px;left:0;width:1200px;height:267px;background:var(--green)}
.footer-line{left:206px;top:108px;width:824px;height:1px;background:rgba(255,255,255,.6)}
.social{top:136px;display:flex;gap:17px;left:518px}
.social span{width:43px;height:42px;background:var(--white);border-radius:2px;display:flex;align-items:center;justify-content:center}
.social span i{width:14px;height:14px;border-radius:50%;background:var(--green)}
.copyright{top:230px;left:0;width:1200px;text-align:center;color:var(--white);font-size:11px}
</style>
</head>
<body>

<header class="site-header abs">
  <nav class="nav nav-left abs"><span>Info</span><span>About</span><span>Gallery</span><span>Links</span></nav>
  <div class="brand abs"><i></i>Lanterns on the Hill</div>
  <nav class="nav nav-right abs"><span>Sponsors</span><span>Store</span><span>Blog</span><span>Contact us</span></nav>
  <div class="cart-btn abs">
    <svg width="18" height="16" viewBox="0 0 18 16" fill="none" stroke="#3bae49" stroke-width="1.5" stroke-linecap="round" stroke-linejoin="round"><path d="M1 1h3l2 9h9l2-6H5"/><circle cx="7" cy="14" r="1"/><circle cx="14" cy="14" r="1"/></svg>
  </div>
</header>

<section class="hero abs" role="img" aria-label="Parade crowd in green cheering along the street beside a decorated float">
  <div class="hero-shade abs"></div>
  <h1 class="hero-title heading abs">The 35th Annual<br>Lanterns on the Hill Parade</h1>
  <p class="hero-text abs">Lorem ipsum dolor sit amet, consectetur adipiscing elit.<br>In vitae turpis eu justo scelerisque cursus.<br>Etiam a diam massa.</p>
  <div class="btn hero-btn abs">More info</div>
  <div class="dots abs"><span></span><span class="on"></span><span></span><span></span><span></span></div>
</section>

<section class="modules">
  <div class="module abs" style="left:187px">
    <div class="module-icon">
      <svg width="72" height="72" viewBox="0 0 72 72" fill="none" stroke="#3bae49" stroke-width="5" stroke-linecap="round" stroke-linejoin="round"><path d="M4 6h10l6 42h40l6-32H17"/><path d="M38 30h14"/><circle cx="26" cy="62" r="3"/><circle cx="54" cy="62" r="3"/></svg>
    </div>
    <div class="module-label">Store</div>
    <div class="btn">Open store</div>
  </div>
  <div class="module abs" style="left:452px">
    <div class="module-icon">
      <svg class="ph" width="124" height="96" role="img" aria-label="Meadowlark Dash 2020 event badge"><rect width="124" height="96" rx="6" fill="#3a9a46"/></svg>
    </div>
    <div class="module-label">Sign up for run</div>
    <div class="btn">Sign up</div>
  </div>
  <div class="module abs" style="left:716px">
    <div class="module-icon">
      <svg class="ph" width="96" height="128" style="margin-top:-32px" role="img" aria-label="Parade magazine cover with crowd photo"><rect width="96" height="128" fill="#5e7a52"/></svg>
    </div>
    <div class="module-label">Magazine</div>
    <div class="btn">Check magazine</div>
  </div>
  <div class="module abs" style="left:999px">
    <div class="module-icon">
      <svg width="76" height="60" viewBox="0 0 76 60" fill="none" stroke="#3bae49" stroke-width="4.5" stroke-linecap="round"><circle cx="38" cy="18" r="11"/><path d="M20 54c2-10 10-15 18-15s16 5 18 15z"/><path d="M16 12a8 8 0 0 0 0 14M60 12a8 8 0 0 1 0 14M6 46c1-6 4-9 8-10M70 46c-1-6-4-9-8-10"/></svg>
    </div>
    <div class="module-label">Participant portal</div>
    <div class="btn">Open portal</div>
  </div>
</section>

<section class="countdown abs">
  <h2 class="band-title heading abs" style="top:46px">Next<br><em>Parade</em><br>Countdown</h2>
  <div class="count abs" style="left:484px"><div class="count-box">185</div><div class="count-label">Days</div></div>
  <div class="count abs" style="left:653px"><div class="count-box">10</div><div class="count-label">Hours</div></div>
  <div class="count abs" style="left:822px"><div class="count-box">59</div><div class="count-label">Minutes</div></div>
  <div class="count abs" style="left:991px"><div class="count-box">39</div><div class="count-label">Seconds</div></div>
</section>

<section class="history">
  <div class="eyebrow abs" style="left:117px;top:1424px">Our history</div>
  <h2 class="story-title heading abs" style="left:117px;top:1452px">Welcome to<br>Lanterns on the Hill Parade</h2>
  <p class="story-text abs" style="left:117px;top:1594px">Lorem ipsum dolor sit amet, consectetur adipiscing elit. Nam quis ipsum ut risus tristique tincidunt. Phasellus porta elementum ante. Suspendisse vel mollis metus, sed mollis mauris. Suspendisse aliquam mollis orci id efficitur. Donec quis volutpat enim. Donec ultricies orci ut ex dapibus, eu suscipit velit laoreet.</p>
  <div class="photo abs" style="left:634px;top:1430px;background:linear-gradient(110deg,#6b3b36 0%,#3e5540 45%,#4a6a45 70%,#7a7a88 100%)" role="img" aria-label="Decorated parade float passing a crowd dressed in green"></div>
</section>

<section class="route">
  <div class="photo abs" style="left:117px;top:1858px;background:linear-gradient(180deg,#3a3a40 0%,#5b5560 50%,#8a8a92 100%)" role="img" aria-label="Runners' legs and shoes crossing a street during a road race"></div>
  <div class="eyebrow abs" style="left:634px;top:1852px">Route</div>
  <h2 class="story-title heading abs" style="left:634px;top:1881px">Meadowlark Dash<br>Virtual Route</h2>
  <p class="story-text abs" style="left:634px;top:2023px">Lorem ipsum dolor sit amet, consectetur adipiscing elit. Nam quis ipsum ut risus tristique tincidunt. Phasellus porta elementum ante. Suspendisse vel mollis metus, sed mollis mauris. Suspendisse aliquam mollis orci id efficitur. Donec quis volutpat enim. Donec ultricies orci ut ex dapibus, eu suscipit velit laoreet.</p>
</section>

<section class="registration abs">
  <h2 class="band-title heading abs" style="left:84px;top:71px;font-size:47px">Runner<br><em>Registration</em></h2>
  <p class="reg-text abs">Lorem ipsum dolor sit amet, consectetur adipiscing elit. Nam quis ipsum ut risus tristique tincidunt. Phasellus porta elementum ante. Suspendisse vel mollis metus, sed mollis mauris.</p>
  <div class="reg-btn abs">REGISTER NOW</div>
</section>

<div class="runners abs" role="img" aria-label="Crowd of runners in green shirts filling a tree-lined street"></div>

<section class="card abs">
  <div class="eyebrow">Subscription</div>
  <h2 class="card-title heading abs">Subscribe for<br>Tomfoolery <em>Bulletin</em></h2>
  <div class="field ok abs"><small>Name and surname</small><b>Rowan Pell</b>
    <svg width="13" height="13" viewBox="0 0 13 13"><circle cx="6.5" cy="6.5" r="6.5" fill="#3bae49"/><path d="M3.5 6.7l2 2 4-4" stroke="#fff" stroke-width="1.5" fill="none"/></svg>
  </div>
  <div class="field email abs">Email</div>
  <div class="btn sub-btn abs">Subscribe</div>
</section>

<footer class="site-footer abs">
  <nav class="nav nav-left abs" style="top:55px;height:0">
    <span>Info</span><span>About</span><span>Gallery</span><span>Links</span></nav>
  <div class="brand abs" style="top:22px">
    <i></i>Lanterns on the Hill</div>
  <nav class="nav nav-right abs" style="top:55px;height:0"><span>Sponsors</span><span>Store</span><span>Blog</span><span>Contact us</span></nav>
  <div class="footer-line abs"></div>
  <div class="social abs">
    <span aria-label="Social link one"><i></i></span><span aria-label="Social link two"><i></i></span><span aria-label="Social link three"><i></i></span>
  </div>
  <p class="copyright abs">© Copyright 2021 The Hollowbrook Group LLC - All right reserved.</p>
</footer>

</body>
</html>
```